iron deficiency anemia - educational reference paper

looking for an educational paper/poster 8x11 or no larger than 11x14 that lists the most common foods with pictures and limited words a super rough outline attached - I wrote the words of the pictures (but would like to have the actual pictures of these items) I would like in roughly the same order
for the pictures for fatigue, headache....can be drawings or cartoons
double sided or single sided (which ever fits) see attached for categories (3 of them)

Target Market(s)

educational for people with limited education - thus not much wording

Requirements
Must have
• pictures, simple design

```html
<!DOCTYPE html>
<html lang="en">
<head>
<meta charset="utf-8">
<title>Iron Deficiency Anemia – Reference Sheet</title>
<link rel="stylesheet" href="https://fonts.googleapis.com/css2?family=Anton&family=Poppins:wght@500;600;800&display=swap">
<style>
  :root {
    --blue: #1e5c8f;
    --navy: #233b5a;
    --navy-deep: #1c3150;
    --band: #22395a;
    --green: #6ab24c;
    --title-blue: #1d5f94;
    --white: #ffffff;
    --disc: #d9d3bd;
    --disc-edge: #b5ad92;
    --backdrop: #d6d6d6;
  }
  * { box-sizing: border-box; margin: 0; padding: 0; }
  html, body { width: 1196px; height: 1200px; overflow: hidden; }
  body {
    background: var(--backdrop);
    font-family: "Poppins", sans-serif;
    position: relative;
  }
  .page {
    position: absolute;
    top: 261px;
    width: 523px;
    height: 677px;
    overflow: hidden;
    background: linear-gradient(90deg, var(--blue) 0%, var(--navy) 100%);
  }
  .page--front { left: 61px; }
  .page--back { left: 612px; }
  .page svg.shape { position: absolute; left: 0; top: 0; }

  .main-title {
    position: absolute; left: 17px; top: 14px;
    font-family: "Anton", sans-serif;
    line-height: 1;
  }
  .main-title__top { display: block; color: var(--title-blue); font-size: 40px; letter-spacing: -0.5px; }
  .main-title__bottom { display: block; color: var(--green); font-size: 62px; margin-top: 2px; letter-spacing: -1px; }

  .section-title {
    position: absolute;
    font-weight: 800;
    color: var(--white);
    line-height: 1.12;
    text-transform: uppercase;
  }
  .section-title .accent { color: var(--green); }
  .section-title--front { right: 16px; top: 48px; text-align: right; font-size: 23px; }
  .section-title--back { left: 0; right: 0; top: 14px; text-align: center; font-size: 23px; }
  .rule { position: absolute; height: 2px; background: var(--white); }

  .food {
    position: absolute;
    width: 86px;
    left: var(--x); top: var(--y);
    transform: translate(-50%, -24px);
    text-align: center;
  }
  .food__pic {
    width: 48px; height: 48px; margin: 0 auto;
    border-radius: 50%;
    border: 3px solid var(--white);
    background: radial-gradient(circle at 40% 38%, #ece7d4 0%, var(--disc) 55%, var(--disc-edge) 100%);
  }
  .food__name {
    margin-top: 4px;
    color: var(--white);
    font-size: 9.3px;
    font-weight: 500;
    line-height: 1.1;
    white-space: nowrap;
  }
  .divider { position: absolute; left: 19px; width: 488px; height: 1px; background: var(--green); }

  .band { position: absolute; left: 0; width: 523px; top: 325px; height: 130px; background: var(--band); }
  .pill {
    position: absolute; left: 114px; top: 311px; width: 295px; height: 28px;
    border-radius: 14px; background: var(--green);
    color: var(--white); font-weight: 800; font-size: 19px;
    text-align: center; line-height: 28px; letter-spacing: 0.2px;
  }
  .symptom {
    position: absolute; top: 363px;
    left: var(--x); transform: translateX(-50%);
    width: 90px; text-align: center;
  }
  .symptom__ring {
    width: 52px; height: 52px; margin: 0 auto;
    border-radius: 50%;
    border: 3px solid var(--blue);
    border-bottom-color: var(--green);
    border-left-color: var(--green);
    transform: rotate(-45deg);
    background: var(--band);
    display: flex; align-items: center; justify-content: center;
  }
  .symptom__icon {
    width: 32px; height: 32px; border-radius: 50%;
    background: #e4e9ef; opacity: 0.85;
    transform: rotate(45deg);
  }
  .symptom__name { margin-top: 6px; color: var(--white); font-size: 9.3px; font-weight: 500; }
  .symptom-link { position: absolute; left: 66px; width: 390px; top: 388px; height: 2px; background: var(--blue); }

  .signs-title {
    position: absolute; left: 0; right: 0; top: 484px;
    text-align: center; color: var(--white);
    font-weight: 800; font-size: 20px;
  }
  .signs-title .accent { color: var(--green); }
  .signs-rule { position: absolute; top: 496px; height: 2px; background: var(--green); }

  .sign {
    position: absolute;
    width: 110px; height: 110px;
    left: var(--x); top: var(--y);
    transform: translate(-50%, -50%);
    border-radius: 50%;
    border: 4px solid var(--white);
    box-shadow: 0 3px 8px rgba(0,0,0,0.35);
  }
  .sign--palm { background: radial-gradient(circle at 50% 45%, #d9b7a0, #b9c6d6 85%); }
  .sign--nail { background: radial-gradient(circle at 50% 50%, #c79a9f, #e2d6d8 85%); }
  .sign--eye { background: radial-gradient(circle at 45% 35%, #d9a79a, #efbaa8 85%); }
  .sign--tongue { background: radial-gradient(circle at 50% 55%, #e4a7a5, #6b4237 85%); }
</style>
</head>
<body>

<!-- Front side -->
<section class="page page--front">
  <svg class="shape" width="523" height="677" viewBox="0 0 523 677" aria-hidden="true">
    <path d="M0 0 H523 V26 C470 8 400 4 350 40 C290 80 250 140 130 148 C70 152 30 140 0 128 Z" fill="var(--white)"/>
    <path d="M523 26 C470 8 400 4 350 40 C290 80 250 140 130 148 C70 152 30 140 0 128" fill="none" stroke="var(--navy-deep)" stroke-width="5"/>
    <path d="M0 646 C60 622 150 608 230 614 C330 622 420 650 523 640 V677 H0 Z" fill="var(--green)"/>
    <path d="M0 646 C60 622 150 608 230 614 C330 622 420 650 523 640" fill="none" stroke="var(--navy-deep)" stroke-width="3"/>
  </svg>

  <h1 class="main-title">
    <span class="main-title__top">IRON DEFICIENCY</span>
    <span class="main-title__bottom">ANEMIA</span>
  </h1>

  <h2 class="section-title section-title--front">Common<br>foods in your<br><span class="accent">community</span></h2>
  <div class="rule" style="left:443px; top:133px; width:64px;"></div>

  <div class="food" style="--x:235px; --y:184px;"><div class="food__pic" role="img" aria-label="Rice bran photo"></div><p class="food__name">Rice Bran</p></div>
  <div class="food" style="--x:296px; --y:184px;"><div class="food__pic" role="img" aria-label="Sheep or lamb photo"></div><p class="food__name">Sheep/lamb</p></div>
  <div class="food" style="--x:357px; --y:184px;"><div class="food__pic" role="img" aria-label="Goose photo"></div><p class="food__name">Goose</p></div>
  <div class="food" style="--x:418px; --y:184px;"><div class="food__pic" role="img" aria-label="Whale meat photo"></div><p class="food__name">Whale</p></div>
  <div class="food" style="--x:479px; --y:184px;"><div class="food__pic" role="img" aria-label="Winged bean photo"></div><p class="food__name">Winged Bean</p></div>
  <div class="divider" style="top:237px;"></div>

  <div class="food" style="--x:55px; --y:275px;"><div class="food__pic" role="img" aria-label="Mung bean photo"></div><p class="food__name">Mung Bean</p></div>
  <div class="food" style="--x:116px; --y:275px;"><div class="food__pic" role="img" aria-label="Lentil photo"></div><p class="food__name">Lentil</p></div>
  <div class="food" style="--x:176px; --y:275px;"><div class="food__pic" role="img" aria-label="Yellow bean photo"></div><p class="food__name">Yellow Bean</p></div>
  <div class="food" style="--x:237px; --y:275px;"><div class="food__pic" role="img" aria-label="White bean photo"></div><p class="food__name">White Bean</p></div>
  <div class="food" style="--x:298px; --y:275px;"><div class="food__pic" role="img" aria-label="Pork photo"></div><p class="food__name">Pig/pork</p></div>
  <div class="food" style="--x:359px; --y:275px;"><div class="food__pic" role="img" aria-label="Kidney bean photo"></div><p class="food__name">Kidney Bean</p></div>
  <div class="food" style="--x:420px; --y:275px;"><div class="food__pic" role="img" aria-label="Cowpea photo"></div><p class="food__name">Cowpea</p></div>
  <div class="food" style="--x:481px; --y:275px;"><div class="food__pic" role="img" aria-label="Black bean photo"></div><p class="food__name">Black Bean</p></div>
  <div class="divider" style="top:329px;"></div>

  <div class="food" style="--x:61px; --y:370px;"><div class="food__pic" role="img" aria-label="Chili or pink bean photo"></div><p class="food__name">Chili/pink Bean</p></div>
  <div class="food" style="--x:122px; --y:370px;"><div class="food__pic" role="img" aria-label="Bagel photo"></div><p class="food__name">Bagel</p></div>
  <div class="food" style="--x:183px; --y:370px;"><div class="food__pic" role="img" aria-label="Chicken and clams photo"></div><p class="food__name">Chicken Clams</p></div>
  <div class="food" style="--x:243px; --y:370px;"><div class="food__pic" role="img" aria-label="Egg photo"></div><p class="food__name">Egg</p></div>
  <div class="food" style="--x:304px; --y:370px;"><div class="food__pic" role="img" aria-label="Lima bean photo"></div><p class="food__name">Lima Bean</p></div>
  <div class="food" style="--x:365px; --y:370px;"><div class="food__pic" role="img" aria-label="Duck photo"></div><p class="food__name">Duck</p></div>
  <div class="food" style="--x:426px; --y:370px;"><div class="food__pic" role="img" aria-label="Pumpkin seed photo"></div><p class="food__name">Pumpkin Seen</p></div>
  <div class="food" style="--x:487px; --y:370px;"><div class="food__pic" role="img" aria-label="Squab photo"></div><p class="food__name">Squab</p></div>
  <div class="divider" style="top:422px;"></div>

  <div class="food" style="--x:48px; --y:461px;"><div class="food__pic" role="img" aria-label="Potato photo"></div><p class="food__name">Potato</p></div>
  <div class="food" style="--x:109px; --y:461px;"><div class="food__pic" role="img" aria-label="Cranberry bean photo"></div><p class="food__name">Cranberry Bean</p></div>
  <div class="food" style="--x:170px; --y:461px;"><div class="food__pic" role="img" aria-label="Nuts photo"></div><p class="food__name">Nuts</p></div>
  <div class="food" style="--x:230px; --y:461px;"><div class="food__pic" role="img" aria-label="Pigeon pea photo"></div><p class="food__name">Pigeon Pea</p></div>
  <div class="food" style="--x:291px; --y:461px;"><div class="food__pic" role="img" aria-label="Turkey photo"></div><p class="food__name">Turkey</p></div>
  <div class="food" style="--x:352px; --y:461px;"><div class="food__pic" role="img" aria-label="Adzuki bean photo"></div><p class="food__name">Aduzki Bean</p></div>
  <div class="food" style="--x:413px; --y:461px;"><div class="food__pic" role="img" aria-label="Beet photo"></div><p class="food__name">Beet</p></div>
  <div class="food" style="--x:474px; --y:461px;"><div class="food__pic" role="img" aria-label="Split peas photo"></div><p class="food__name">Masa Split Peas</p></div>
  <div class="divider" style="top:514px;"></div>

  <div class="food" style="--x:53px; --y:554px;"><div class="food__pic" role="img" aria-label="Carrot photo"></div><p class="food__name">Carrot</p></div>
  <div class="food" style="--x:114px; --y:554px;"><div class="food__pic" role="img" aria-label="Cuttlefish photo"></div><p class="food__name">Cuttlefish Bear</p></div>
  <div class="food" style="--x:175px; --y:554px;"><div class="food__pic" role="img" aria-label="Tortilla photo"></div><p class="food__name">Tortilla</p></div>
  <div class="food" style="--x:236px; --y:554px;"><div class="food__pic" role="img" aria-label="Yardlong bean photo"></div><p class="food__name">Yardlong Bean</p></div>
  <div class="food" style="--x:297px; --y:554px;"><div class="food__pic" role="img" aria-label="Sardines photo"></div><p class="food__name">Sardines</p></div>
  <div class="food" style="--x:358px; --y:554px;"><div class="food__pic" role="img" aria-label="Sesame seed photo"></div><p class="food__name">Sesame Seed</p></div>
  <div class="food" style="--x:419px; --y:554px;"><div class="food__pic" role="img" aria-label="Spinach photo"></div><p class="food__name">Spinach</p></div>
  <div class="food" style="--x:479px; --y:554px;"><div class="food__pic" role="img" aria-label="Fava bean photo"></div><p class="food__name">Fava Bean</p></div>
</section>

<!-- Back side -->
<section class="page page--back">
  <svg class="shape" width="523" height="677" viewBox="0 0 523 677" aria-hidden="true">
    <path d="M0 587 C90 580 170 598 250 618 C340 640 430 628 523 605 V677 H0 Z" fill="var(--green)"/>
  </svg>

  <h2 class="section-title section-title--back">Common foods in<br><span class="accent">your community</span></h2>
  <div class="rule" style="left:229px; top:74px; width:64px;"></div>

  <div class="food" style="--x:48px; --y:126px;"><div class="food__pic" role="img" aria-label="Tomato photo"></div><p class="food__name">Tomato</p></div>
  <div class="food" style="--x:109px; --y:126px;"><div class="food__pic" role="img" aria-label="Sunflower seed photo"></div><p class="food__name">Sunflower Seed</p></div>
  <div class="food" style="--x:170px; --y:126px;"><div class="food__pic" role="img" aria-label="Shrimp photo"></div><p class="food__name">Shrimp</p></div>
  <div class="food" style="--x:230px; --y:126px;"><div class="food__pic" role="img" aria-label="Blackberry photo"></div><p class="food__name">Blackberry</p></div>
  <div class="food" style="--x:290px; --y:126px;"><div class="food__pic" role="img" aria-label="Cauliflower photo"></div><p class="food__name">Califlower</p></div>
  <div class="food" style="--x:352px; --y:126px;"><div class="food__pic" role="img" aria-label="Mushrooms photo"></div><p class="food__name">Mushrooms</p></div>
  <div class="food" style="--x:413px; --y:126px;"><div class="food__pic" role="img" aria-label="Halibut photo"></div><p class="food__name">Halibut</p></div>
  <div class="food" style="--x:474px; --y:126px;"><div class="food__pic" role="img" aria-label="Brussels sprouts photo"></div><p class="food__name">Brussle Sprouts</p></div>
  <div class="divider" style="top:181px;"></div>

  <div class="food" style="--x:175px; --y:221px;"><div class="food__pic" role="img" aria-label="Collard greens photo"></div><p class="food__name">Collard Greens</p></div>
  <div class="food" style="--x:236px; --y:221px;"><div class="food__pic" role="img" aria-label="Broccoli photo"></div><p class="food__name">Broccoli</p></div>
  <div class="food" style="--x:297px; --y:221px;"><div class="food__pic" role="img" aria-label="Chickpeas photo"></div><p class="food__name">Ckickpeas</p></div>
  <div class="food" style="--x:358px; --y:221px;"><div class="food__pic" role="img" aria-label="Natto, teff and amaranth photo"></div><p class="food__name">Natto Teff<br>Amaranth</p></div>

  <div class="band"></div>
  <h3 class="pill">SYMPTOMS OF ANEMIA</h3>
  <div class="symptom-link"></div>
  <div class="symptom" style="--x:66px;"><div class="symptom__ring"><div class="symptom__icon" role="img" aria-label="Fatigue icon"></div></div><p class="symptom__name">Fatigue</p></div>
  <div class="symptom" style="--x:164px;"><div class="symptom__ring"><div class="symptom__icon" role="img" aria-label="Headache icon"></div></div><p class="symptom__name">Headache</p></div>
  <div class="symptom" style="--x:261px;"><div class="symptom__ring"><div class="symptom__icon" role="img" aria-label="Dizziness icon"></div></div><p class="symptom__name">Dizziness</p></div>
  <div class="symptom" style="--x:358px;"><div class="symptom__ring"><div class="symptom__icon" role="img" aria-label="Blurry vision icon"></div></div><p class="symptom__name">Blurry Vision</p></div>
  <div class="symptom" style="--x:456px;"><div class="symptom__ring"><div class="symptom__icon" role="img" aria-label="Muscle weakness icon"></div></div><p class="symptom__name">Muscle Weakness</p></div>

  <div class="signs-rule" style="left:0; width:151px;"></div>
  <div class="signs-rule" style="left:372px; width:151px;"></div>
  <h3 class="signs-title">SIGNS OF <span class="accent">ANEMIA</span></h3>

  <div class="sign sign--palm" style="--x:76px; --y:581px;" role="img" aria-label="Photo of a pale palm"></div>
  <div class="sign sign--nail" style="--x:203px; --y:593px;" role="img" aria-label="Photo of brittle, spoon-shaped fingernails"></div>
  <div class="sign sign--eye" style="--x:325px; --y:602px;" role="img" aria-label="Photo of a pale inner eyelid"></div>
  <div class="sign sign--tongue" style="--x:447px; --y:596px;" role="img" aria-label="Photo of a pale, smooth tongue"></div>
</section>

</body>
</html>
```